Landing page for buying gold and stamps

Create a landing page for our purchase. We buy postage stamps, franked goods, gold coins, scrap gold, silver money, etc. We don't want to sell anything to people, we just shop. So the visitors should send their old gold, their stamps, etc. by post. We then estimate the value and transfer the money by bank or you can collect it in cash.

The visitor should see what he can sell. If he fills in his contact details, he will receive our purchase form and the mailing label by post so that he can send in his sales goods free of charge. Or he can call us or write an e-mail and come to us directly.

We buy:
When the form is filled out, an email will be sent to our address with the following data:
Surname
First name
Street, Nr.
Post loan number
place
What do you want to sell

In the appendix I have added designs of flyers. You can see what we buy on it. What is missing on the flyer, however, are stamps, franking goods and rarities. In addition, the design should be similar. The logo can also be used.

In addition, the following text should be on the page:
Do you need help selling an inherited collection? Feel free to contact us. We are happy to help. We have been in the stamp and coin trade for nearly 100 years.

I have also attached a picture of the stamp as an attachment. This should also be put on the side with old gold and gold coins.

And here you will find our current purchase pages:
https://www.briefhaus-tanner.ch/ankauf-gold-und-silber
https://www.briefhaus-tanner.ch/ankauf-frankatur

Competitors' pages:
https://www.edelwertplatz.ch/goldankauf/
https://www.talerbruhin.ch/ankauf-1/altgold-ankauf1.html?gclid=Xq7RtLwPzN2vKdFaYbHsUmEcGjTnQoVrZiBxWkLpDyAsCfNhMuJbOeTgIlKwSvHaRdYqPzXnBmCtGuFoLiEkJrQsWvTy

Target Market(s)

Private persons

Font styles to use
Serif
Sans Serif

Requirements
Must have
• It must be clear that anyone who wants to sell their gold, stamps or coins can do so easily from home by post. You no longer have to go to a store.
Steps to Sell:
1. You fill out your contact details
2. We will send you a form and a label for shipping (no postage for you!)
3. You will receive a non-binding purchase offer
4. You will receive the money transferred or you can collect it in cash (or we will send you the valuables you have sent back)

You have no costs! Simply sell your gold or stamps from home.

```html
<!DOCTYPE html>
<html lang="en">
<head>
<meta charset="utf-8">
<title>Briefhaus Tanner – We buy stamps, gold and more</title>
<link href="https://fonts.googleapis.com/css2?family=Libre+Caslon+Text:wght@400&family=Inter:wght@400;500;600;700&display=swap" rel="stylesheet">
<style>
:root{
  --navy:#2b2d8c;
  --red:#e31b23;
  --ink:#2a2a2a;
  --muted:#555;
  --soft:#eeeef3;
  --soft2:#f4f5f9;
  --grey:#ebebeb;
  --line:#d9d9e0;
  --circle:#f3f3f5;
}
*{box-sizing:border-box;margin:0;padding:0}
html,body{width:1200px;height:3760px;overflow:hidden}
body{font-family:"Inter",Arial,sans-serif;color:var(--ink);background:#fff;position:relative}
.serif{font-family:"Libre Caslon Text",Georgia,serif;font-weight:400}
.wrap{position:absolute;left:0;width:1200px}

/* top bar */
.topbar{top:0;height:35px;background:var(--navy);color:#fff;font-size:13px;font-weight:500}
.topbar .item{position:absolute;top:10px;display:flex;align-items:center;gap:8px}
.topbar .sep{position:absolute;left:913px;top:9px;width:1px;height:17px;background:rgba(255,255,255,.6)}

/* header */
.header{top:35px;height:62px;border-bottom:1px solid #eee}
.brand{position:absolute;left:101px;top:19px;font-size:19px;font-weight:700;color:var(--navy);display:flex;align-items:center;gap:8px}
.brand .mark{width:14px;height:14px;background:var(--red)}
.nav{position:absolute;left:378px;top:24px;display:flex;gap:31px;font-size:13px;color:#333}
.nav .active{color:var(--navy);font-weight:700}
.cta{position:absolute;left:963px;top:15px;width:136px;height:35px;background:var(--red);color:#fff;font-size:13px;font-weight:700;display:flex;align-items:center;justify-content:center;border-radius:2px}

/* hero */
.hero{top:97px;height:388px}
.hero h1{position:absolute;left:101px;top:115px;width:520px;font-size:40px;line-height:49px;color:#222;letter-spacing:-.5px}
.hero .visual{position:absolute;left:608px;top:58px;width:410px;height:275px;border-radius:6px 140px 140px 6px;background:linear-gradient(120deg,#5b6f52 0%,#3d5a4e 40%,#d9b44a 70%,#b9932e 100%)}

/* what we buy */
.buy{top:485px;height:565px;background:var(--soft)}
.buy h2{position:absolute;left:101px;top:52px;font-size:40px;color:#222}
.card{position:absolute;top:135px;width:323px;height:365px;background:#fff;text-align:center;border-bottom:7px solid var(--navy)}
.card.red{border-bottom-color:var(--red)}
.card .pic{width:150px;height:165px;margin:33px auto 0}
.card h3{font-size:21px;font-weight:500;margin-top:22px;color:#222}
.card p{font-size:13.5px;line-height:21px;color:#444;margin:10px 24px 0}

/* how to sell */
.how{top:1050px;height:598px}
.how h2{position:absolute;left:0;width:1200px;text-align:center;top:70px;font-size:42px;color:#222}
.how .lead{position:absolute;left:0;width:1200px;text-align:center;top:142px;font-size:17px;color:#333}
.step{position:absolute;top:210px;width:230px;text-align:center}
.step .ico{width:168px;height:168px;border-radius:50%;background:var(--circle);margin:0 auto;display:flex;align-items:center;justify-content:center}
.step p{font-size:13.5px;line-height:21px;color:#333;margin:22px 22px 0}

/* why */
.why{top:1648px;height:444px;background:linear-gradient(90deg,var(--soft2),#fff 80%)}
.why .box{position:absolute;left:101px;top:70px;width:491px;height:307px;background:#fff;border:1px solid #e5e5ea;border-top:3px solid var(--red);padding:40px 28px}
.why .kicker{font-size:10px;letter-spacing:1.5px;font-weight:600}
.why h2{font-size:40px;line-height:49px;margin-top:12px;color:#222}
.why p{font-size:13.5px;line-height:21px;color:#444;margin-top:18px}
.why .photo{position:absolute;left:765px;top:85px;width:305px;height:280px;border-radius:40% 30% 20% 45%;background:radial-gradient(circle at 45% 60%,#d8d8d8 0%,#c4a04a 35%,#b8913a 60%,#f1efe9 100%)}

/* faq */
.faq{top:2092px;height:553px}
.faq h2{position:absolute;left:0;width:1200px;text-align:center;top:48px;font-size:42px;color:#222}
.faq .list{position:absolute;left:354px;top:132px;width:492px}
.faq .q{height:71px;border-bottom:1px solid var(--line);display:flex;align-items:center;justify-content:space-between;padding:0 22px;font-size:17px;font-weight:600;color:#222}
.faq .q.open{color:var(--red)}
.faq .a{padding:20px 22px 24px;font-size:13.5px;line-height:21px;color:#555;border-bottom:1px solid var(--line)}
.faq .pm{color:#999;font-size:26px;font-weight:300}

/* contact */
.contact{top:2645px;height:760px;background:var(--grey)}
.contact .kicker{position:absolute;left:0;width:1200px;text-align:center;top:71px;font-size:10px;letter-spacing:1.5px;font-weight:600}
.contact h2{position:absolute;left:0;width:1200px;text-align:center;top:97px;font-size:35px;line-height:50px;color:#222}
.contact .lead{position:absolute;left:0;width:1200px;text-align:center;top:212px;font-size:14px;color:#333}
.form{position:absolute;left:354px;top:260px;width:492px}
.field{height:49px;background:#fff;margin-bottom:11px;position:relative;padding:9px 14px}
.field label{display:block;font-size:8px;color:#999;letter-spacing:.5px}
.field .val{font-size:14px;color:#222;margin-top:3px}
.field.focus{border-bottom:2px solid var(--navy)}
.field.select{display:flex;align-items:center;justify-content:space-between;font-size:14px;color:#333}
.submit{position:absolute;left:182px;top:394px;width:128px;height:34px;background:var(--navy);color:#fff;font-size:13px;font-weight:700;display:flex;align-items:center;justify-content:center;border-radius:2px}

/* footer */
.footer{top:3405px;height:321px}
.footer .brand{top:65px}
.fcol{position:absolute;top:62px;font-size:15px;color:#333}
.fcol h4{font-size:15px;font-weight:600;margin-bottom:12px;color:#222}
.fcol li{list-style:none;height:39px}
.fcol .row{display:flex;gap:14px;align-items:flex-start;height:39px}
.totop{position:absolute;left:1121px;top:62px;width:28px;height:28px;border:1px solid #999;display:flex;align-items:center;justify-content:center}
.bottombar{top:3726px;height:34px;background:var(--navy);color:#fff;font-size:12px;font-weight:600}
.bottombar .follow{position:absolute;left:101px;top:10px;display:flex;align-items:center;gap:12px}
.bottombar .dot{width:9px;height:9px;border-radius:50%;background:#fff}
.bottombar .copy{position:absolute;left:486px;top:10px}
</style>
</head>
<body>

<div class="wrap topbar">
  <div class="item" style="left:101px">
    <svg width="12" height="15" viewBox="0 0 12 15"><path d="M6 0a6 6 0 0 0-6 6c0 4.5 6 9 6 9s6-4.5 6-9a6 6 0 0 0-6-6zm0 8.3A2.3 2.3 0 1 1 6 3.7a2.3 2.3 0 0 1 0 4.6z" fill="#fff"/></svg>
    Werkgasse 14, 4931 Feldbach
  </div>
  <div class="item" style="left:766px">
    <svg width="14" height="14" viewBox="0 0 24 24"><path d="M6.6 10.8a15 15 0 0 0 6.6 6.6l2.2-2.2a1 1 0 0 1 1-.25 11.4 11.4 0 0 0 3.6.57 1 1 0 0 1 1 1V20a1 1 0 0 1-1 1A17 17 0 0 1 3 4a1 1 0 0 1 1-1h3.5a1 1 0 0 1 1 1c0 1.25.2 2.45.57 3.57a1 1 0 0 1-.25 1z" fill="#fff"/></svg>
    0041 61 555 01 20
  </div>
  <div class="sep"></div>
  <div class="item" style="left:935px">
    <svg width="14" height="11" viewBox="0 0 14 11"><rect width="14" height="11" rx="1.5" fill="#fff"/><path d="M1 1.5l6 4.5 6-4.5" stroke="#2b2d8c" stroke-width="1.4" fill="none"/></svg>
    info@briefhaus-tanner.ch
  </div>
</div>

<header class="wrap header">
  <div class="brand"><span class="mark"></span>Briefhaus Tanner</div>
  <nav class="nav">
    <span class="active">Home</span><span>What we Buy</span><span>How to Sell</span><span>Why Choose Us</span><span>FAQ</span>
  </nav>
  <div class="cta">Start Selling</div>
</header>

<section class="wrap hero">
  <h1 class="serif">Your partner for postage<br>stamp, gold coins and<br>much more.</h1>
  <div class="visual" role="img" aria-label="Swiss postage stamps beside a gold coin set"></div>
</section>

<section class="wrap buy">
  <h2 class="serif">What we buy</h2>
  <div class="card" style="left:101px">
    <div class="pic" role="img" aria-label="Historic red and blue postage stamp" style="background:linear-gradient(135deg,#c94a3e,#6f8fb0 60%,#d9c9a8)"></div>
    <h3>Postage Stamp</h3>
    <p>We look for worldwide local and revenue stamps.</p>
  </div>
  <div class="card red" style="left:438px">
    <div class="pic" role="img" aria-label="Gold coin set in a round silver frame" style="border-radius:50%;width:150px;height:150px;margin-top:40px;margin-bottom:15px;background:radial-gradient(circle,#cfcfcf 20%,#d7b24a 60%,#b58c2c)"></div>
    <h3>Gold &amp; Silver</h3>
    <p>We purchase Goldvreneli, old gold and silver, coins, bars, medals, watches, rings, chains</p>
  </div>
  <div class="card" style="left:775px">
    <div class="pic" role="img" aria-label="Old franked postcard with a printed town scene" style="width:110px;background:linear-gradient(180deg,#e4e1da,#7d7a74)"></div>
    <h3>Other Type of Goods</h3>
    <p>We buy franked goods in Switzerland, sorted by value or in sheets. We are currently remunerating around 70% of the nominal value (excluding surcharges).</p>
  </div>
</section>

<section class="wrap how">
  <h2 class="serif">How to sell</h2>
  <p class="lead">You have no costs! Simply sell your gold or stamps from home.</p>
  <div class="step" style="left:105px">
    <div class="ico"><svg width="56" height="62" viewBox="0 0 56 62"><path d="M2 0h30l12 12v46H2z" fill="#2b2d8c"/><rect x="10" y="22" width="24" height="3" fill="#fff"/><rect x="10" y="30" width="18" height="3" fill="#fff"/><rect x="10" y="38" width="14" height="3" fill="#fff"/><circle cx="46" cy="46" r="5" fill="#e31b23"/><path d="M36 62a10 8 0 0 1 20 0z" fill="#e31b23"/></svg></div>
    <p>You fill out your contact details</p>
  </div>
  <div class="step" style="left:358px">
    <div class="ico"><svg width="68" height="50" viewBox="0 0 68 50"><path d="M0 18L14 4h12v12L12 30z" fill="#e31b23"/><circle cx="20" cy="10" r="2.5" fill="#fff"/><path d="M22 20h16l8 8 8-8h14v30H22z" fill="#2b2d8c"/><path d="M54 0h14v20H54z" fill="#2b2d8c"/><rect x="28" y="38" width="34" height="4" fill="#fff"/></svg></div>
    <p>We will send you a form and a label for shipping (no postage for you!)</p>
  </div>
  <div class="step" style="left:611px">
    <div class="ico"><svg width="56" height="60" viewBox="0 0 56 60"><rect x="4" y="0" width="44" height="20" fill="#2b2d8c"/><rect x="10" y="7" width="18" height="3" fill="#fff"/><rect x="0" y="22" width="56" height="14" fill="#e31b23"/><rect x="8" y="38" width="44" height="22" fill="#2b2d8c"/><rect x="14" y="45" width="14" height="3" fill="#fff"/><text x="38" y="53" font-size="10" fill="#fff" font-family="Inter,sans-serif" font-weight="700">$</text></svg></div>
    <p>You will receive a non-binding purchase offer</p>
  </div>
  <div class="step" style="left:864px">
    <div class="ico"><svg width="62" height="60" viewBox="0 0 62 60"><circle cx="42" cy="14" r="14" fill="#e31b23"/><text x="37" y="20" font-size="16" fill="#fff" font-family="Inter,sans-serif" font-weight="700">$</text><rect x="0" y="34" width="9" height="24" fill="#2b2d8c"/><path d="M12 36h22a6 6 0 0 1 0 12H22v2h24l14-10v10l-12 8H12z" fill="#2b2d8c"/></svg></div>
    <p>You will receive the money transferred or you can collect it in cash (or we will send you the valuables you have sent back)</p>
  </div>
</section>

<section class="wrap why">
  <div class="box">
    <div class="kicker">WHY CHOOSE US</div>
    <h2 class="serif">We buy things at the best price.</h2>
    <p>Lorem ipsum dolor sit amet, consetetur sadipscing elitr, sed diam nonumy eirmod tempor invidunt ut labore et dolore magna aliquyam erat, sed diam voluptua. At vero eos et accusam et justo duo dolores et ea rebum. Stet clita kasd</p>
  </div>
  <div class="photo" role="img" aria-label="Stack of gold and silver coins"></div>
</section>

<section class="wrap faq">
  <h2 class="serif">Frequently Asked Question</h2>
  <div class="list">
    <div class="q open">What products Briefhaus-Tanner buy?<span class="pm">&minus;</span></div>
    <div class="a">Lorem ipsum dolor sit amet, consetetur sadipscing elitr, sed diam nonumy eirmod tempor invidunt ut labore et dolore magna aliquyam erat, sed diam voluptua. At vero eos et accusam et justo duo dolores et ea rebum. Stet clita kasd gubergren, no sea</div>
    <div class="q">How can I sell things to Briefhaus-Tanner?<span class="pm">+</span></div>
    <div class="q">How long I can receive money for good?<span class="pm">+</span></div>
  </div>
</section>

<section class="wrap contact">
  <div class="kicker">CONTACT US</div>
  <h2 class="serif">Need help selling an inherited collection?<br>Feel free to contact us</h2>
  <p class="lead">We have been in the stamp and coin trade for nearly 100 years.</p>
  <form class="form">
    <div class="field select">What do you want to sell?
      <svg width="14" height="8" viewBox="0 0 14 8"><path d="M1 1l6 6 6-6" stroke="#999" fill="none"/></svg></div>
    <div class="field focus"><label>SURNAME</label><div class="val">Hofer</div></div>
    <div class="field"><label>FIRSTNAME</label><div class="val">Nina</div></div>
    <div class="field"><label>PLACE</label></div>
    <div class="field"><label>ADDRESS</label></div>
    <div class="field"><label>POST LOAN NO.</label></div>
    <div class="submit">Submit</div>
  </form>
</section>

<footer class="wrap footer">
  <div class="brand"><span class="mark"></span>Briefhaus Tanner</div>
  <div class="fcol" style="left:438px">
    <h4>QuickLink</h4>
    <ul><li>Home</li><li>What We Buy</li><li>How to Sell</li><li>Why Choose Us</li><li>Contact</li></ul>
  </div>
  <div class="fcol" style="left:607px">
    <h4>Contact Us</h4>
    <div class="row"><svg width="16" height="16" viewBox="0 0 24 24"><path d="M6.6 10.8a15 15 0 0 0 6.6 6.6l2.2-2.2a1 1 0 0 1 1-.25 11.4 11.4 0 0 0 3.6.57 1 1 0 0 1 1 1V20a1 1 0 0 1-1 1A17 17 0 0 1 3 4a1 1 0 0 1 1-1h3.5a1 1 0 0 1 1 1c0 1.25.2 2.45.57 3.57a1 1 0 0 1-.25 1z" fill="#aaa"/></svg>0041 61 555 01 20</div>
    <div class="row"><svg width="16" height="13" viewBox="0 0 14 11"><rect width="14" height="11" rx="1.5" fill="#aaa"/><path d="M1 1.5l6 4.5 6-4.5" stroke="#fff" stroke-width="1.4" fill="none"/></svg>info@briefhaus-tanner.ch</div>
    <div class="row"><svg width="16" height="18" viewBox="0 0 12 15"><path d="M6 0a6 6 0 0 0-6 6c0 4.5 6 9 6 9s6-4.5 6-9a6 6 0 0 0-6-6zm0 8.3A2.3 2.3 0 1 1 6 3.7a2.3 2.3 0 0 1 0 4.6z" fill="#aaa"/></svg><span>Werkgasse 14, 4931<br>Feldbach</span></div>
  </div>
  <div class="fcol" style="left:860px">
    <h4>Opening Hours</h4>
    <ul><li>Mon - Fri: 9:AM - 5:PM</li><li>Weekends: 10:AM - 4:PM</li></ul>
  </div>
  <div class="totop"><svg width="12" height="7" viewBox="0 0 12 7"><path d="M1 6l5-5 5 5" stroke="#555" fill="none"/></svg></div>
</footer>

<div class="wrap bottombar">
  <div class="follow">Follow us on <span class="dot"></span><span class="dot"></span><span class="dot"></span></div>
  <div class="copy">2020 Briefhaus Tanner. All Right Reserved</div>
</div>

</body>
</html>
```